Website for Youth Orchestra to sell tickets and attract young musicians

We are looking for a new website design for a Youth Orchestra; one of the best classical youth orchestras in the county. This project is the design only. <br/><br/>The website serves two main purposes:<br/>• Selling tickets for concerts and performances of the orchestra<br/>• Recruiting young musicians to do audition for the orchestra<br/>
Updates

Target Market(s)

Classical music lovers with a special interest in young upcoming musicians.
Young talented musicians

Number of Pages Required

2 page

Colors
ec1f27

Requirements
Must have
• - A Picture on the front page that promotes the main upcomming event
• - Attention for recruiting new musicians
• - Pictures with young musicians (white back ground, see examples)
• - Responsive
• - Please use the logo attached
Should not have
• The brown colors of the current website (kvb-veldhorst.example)

```html
<!DOCTYPE html>
<html lang="en">
<head>
<meta charset="utf-8">
<title>Eemvallei Orkest – Youth Orchestra</title>
<link href="https://fonts.googleapis.com/css2?family=Righteous&family=Roboto:wght@300;400;500;700&display=swap" rel="stylesheet">
<style>
:root{
  --red:#ec1f27;
  --dark:#222222;
  --ink:#1c1c1c;
  --text:#3a3a3a;
  --white:#ffffff;
  --lilac:#f4f1f8;
}
*{margin:0;padding:0;box-sizing:border-box}
html,body{width:1200px;height:3220px;overflow:hidden}
body{position:relative;background:var(--white);font-family:'Roboto',sans-serif;color:var(--text)}
.abs{position:absolute}
.display{font-family:'Righteous',sans-serif;color:var(--ink)}
.pill{position:absolute;background:var(--red);color:var(--white);border-radius:24px;font-family:'Righteous',sans-serif;display:flex;align-items:center;justify-content:center;letter-spacing:.5px}

/* hero */
.hero{left:0;top:0;width:1200px;height:750px;background:linear-gradient(120deg,#d9d7d3 0%,#c9bfb6 40%,#8c5a3c 65%,#d6d3cf 100%)}
.brand{left:55px;top:95px;display:flex;align-items:center;gap:10px}
.brand-mark{width:22px;height:22px;background:var(--red)}
.brand-name{font-family:'Roboto',sans-serif;font-weight:400;font-size:18px;line-height:22px;color:#3a3a3a;white-space:nowrap}
.lang{left:943px;top:48px;font-size:16px;color:#444}
.social-top{left:1014px;top:52px;display:flex;gap:8px}
.dot{width:12px;height:12px;border-radius:50%;background:#777}
.menu-btn{left:1104px;top:23px;width:65px;height:65px;background:var(--red);display:flex;flex-direction:column;justify-content:center;align-items:center;gap:4px}
.menu-btn span{width:20px;height:3px;background:var(--white)}
.hero-title{left:0;top:410px;width:1200px;text-align:center;font-size:80px;color:var(--white);letter-spacing:2px;text-shadow:0 3px 6px rgba(0,0,0,.35)}
.hero-sub{left:350px;top:520px;width:501px;height:44px;background:#151515;color:#fff;font-size:19px;font-weight:300;display:flex;align-items:center;justify-content:center}

/* about */
.about-bg{left:0;top:750px;width:1200px;height:592px;background:linear-gradient(135deg,#fff 40%,var(--lilac) 100%)}
.about-panel{left:0;top:750px;width:496px;height:592px;background:linear-gradient(160deg,#c4222b 0%,#7a1c2a 45%,#182030 100%)}
.about-photo{left:22px;top:850px;width:494px;height:399px;background:radial-gradient(circle at 45% 40%,#7a5a48 0%,#2a2020 40%,#050505 75%)}
.about-title{left:611px;top:910px;font-size:60px}
.about-copy{left:611px;top:1000px;width:465px;font-size:12.6px;line-height:21px;color:#333}
.about-copy p{margin-bottom:17px}

/* events */
.events-bg{left:0;top:1342px;width:1200px;height:573px;background:linear-gradient(100deg,var(--lilac) 0%,#fff 45%)}
.events-title{left:165px;top:1475px;font-size:62px;line-height:78px}
.arrows{left:252px;top:1664px}
.card{position:absolute;top:1426px;width:271px;height:463px;background:var(--red);color:#fff}
.card-photo{width:271px;height:343px}
.card-date{position:absolute;left:15px;top:368px;font-size:13px}
.card-name{position:absolute;left:15px;top:390px;font-size:16px;font-weight:700}
.card-more{position:absolute;left:18px;top:432px;font-family:'Righteous',sans-serif;font-size:13px;display:flex;align-items:center;gap:6px}

/* gallery */
.gallery-title{left:0;top:1975px;width:1200px;text-align:center;font-size:60px}
.tile{position:absolute}

/* footer */
.footer{left:0;top:2817px;width:1200px;height:403px;background:var(--dark)}
.foot-head{position:absolute;font-family:'Righteous',sans-serif;font-size:19px;color:var(--white)}
.foot-head::after{content:"";position:absolute;left:0;top:34px;width:52px;height:2px;background:var(--white)}
.foot-line{position:absolute;font-size:13.5px;line-height:21px;display:flex;gap:10px;color:var(--white)}
.foot-line span{color:var(--white)}
.foot-social{left:212px;top:3070px;display:flex;gap:13px}
.foot-social span{width:9px;height:9px;border-radius:50%;background:var(--white)}
.email-field{left:465px;top:2977px;width:269px;height:33px;background:#3a3a3a;color:#ddd;font-size:12px;padding:9px 10px}
.subscribe{left:465px;top:3015px;width:269px;height:35px;background:var(--red);font-family:'Righteous',sans-serif;font-size:13px;display:flex;align-items:center;justify-content:center;color:#fff}
.page-box{left:760px;top:2877px;width:289px;height:224px;background:#fff}
.page-cover{position:absolute;left:0;top:0;width:289px;height:140px;background:linear-gradient(135deg,#5b6678,#c89a70 55%,#2e3340)}
.page-name{position:absolute;left:66px;top:26px;font-size:13px;font-weight:700;color:#fff}
.page-likes{position:absolute;left:66px;top:46px;font-size:11px;color:#fff}
.page-thumb{position:absolute;left:10px;top:10px;width:46px;height:46px;background:#fff;border:1px solid #ccc}
.mini-btn{position:absolute;top:115px;height:16px;font-size:9px;padding:2px 6px;background:#f2f2f2;color:#333;border-radius:2px}
.friends{position:absolute;left:10px;top:160px;width:269px;height:50px;border:1px solid #e4e4e4;font-size:9px;color:#777;padding:4px 6px}
.faces{display:flex;gap:3px;margin-top:4px}
.faces span{width:22px;height:22px;background:#b8c2cc}
.copyright{left:192px;top:3186px;font-size:12px;color:#fff}
</style>
</head>
<body>

<section class="abs hero" role="img" aria-label="Young woman playing violin, hero photo for the New Year concert"></section>
<header>
  <div class="abs brand"><div class="brand-mark"></div><div class="brand-name">Eemvallei Orkest</div></div>
  <div class="abs lang">EN &#8964;</div>
  <div class="abs social-top"><span class="dot"></span><span class="dot"></span><span class="dot"></span></div>
  <div class="abs menu-btn"><span></span><span></span><span></span></div>
</header>
<h1 class="abs display hero-title">NEW YEAR CONCERT</h1>
<div class="abs hero-sub">Best classical youth orchestras in the country</div>
<a class="pill" style="left:518px;top:602px;width:163px;height:46px;font-size:16px">BUY TICKETS</a>

<section>
  <div class="abs about-bg"></div>
  <div class="abs about-panel" role="img" aria-label="Red and navy low-poly background"></div>
  <div class="abs about-photo" role="img" aria-label="Young girl playing violin on a dark stage"></div>
  <h2 class="abs display about-title">About Us</h2>
  <div class="abs about-copy">
    <p>Quis autem vel eum iure reprehenderit qui in ea voluptate velit esse quam nihil molestiae consequatur, vel illum qui dolorem eum fugiat quo voluptas.</p>
    <p>Itaque earum rerum hic tenetur a sapiente delectus, ut aut reiciendis voluptatibus maiores alias consequatur aut perferendis doloribus asperiores repellat.Nam libero tempore, cum soluta nobis est eligendi optio cumque nihil impedit quo minus id quod maxime placeat facere possimus</p>
    <p>Nam libero tempore, cum soluta nobis est eligendi optio cumque nihil impedit quo minus id quod maxime placeat facere possimus, omnis voluptas assumenda est, omnis dolor repellendus. Temporibus autem quibusdam et aut officiis debitis aut rerum necessitatibus saepe eveniet ut et voluptates .</p>
  </div>
  <a class="pill" style="left:612px;top:1277px;width:135px;height:34px;font-size:13px">REGISTER NOW</a>
</section>

<section>
  <div class="abs events-bg"></div>
  <h2 class="abs display events-title">Upcoming<br>Events</h2>
  <svg class="abs arrows" width="40" height="28" viewBox="0 0 40 28" fill="none" stroke="#111" stroke-width="2.5"><path d="M14 4 L5 14 L14 24"/><path d="M26 4 L35 14 L26 24"/></svg>
  <a class="pill" style="left:204px;top:1735px;width:134px;height:33px;font-size:13px">BUY TICKETS</a>

  <article class="card" style="left:513px">
    <div class="card-photo" role="img" aria-label="Curly-haired violinist performing on black background" style="background:radial-gradient(circle at 40% 35%,#d8cbb8 0%,#5a4a40 35%,#0c0c0c 70%)"></div>
    <div class="card-date">January 5, 2020 &nbsp;&nbsp;( 8.00 PM )</div>
    <div class="card-name">Reiciendis Voluptatibus</div>
    <div class="card-more">MORE INFO <svg width="6" height="8"><path d="M0 0 L6 4 L0 8Z" fill="#fff"/></svg></div>
  </article>
  <article class="card" style="left:806px">
    <div class="card-photo" role="img" aria-label="Violinist in black on a light background" style="background:linear-gradient(180deg,#e6ddd2 0%,#c9a98a 45%,#1a1a1a 90%)"></div>
    <div class="card-date">January 7, 2020 &nbsp;&nbsp;( 8.00 PM )</div>
    <div class="card-name">Alias Consequatur</div>
    <div class="card-more">MORE INFO <svg width="6" height="8"><path d="M0 0 L6 4 L0 8Z" fill="#fff"/></svg></div>
  </article>
</section>

<section>
  <h2 class="abs display gallery-title">Gallery</h2>
  <div class="tile" role="img" aria-label="Violinist in a floral dress by the sea" style="left:0;top:2102px;width:395px;height:415px;background:linear-gradient(160deg,#f2ebe2,#d9c2a8 55%,#b7a999)"></div>
  <div class="tile" role="img" aria-label="Close-up of violin and bow" style="left:0;top:2517px;width:395px;height:300px;background:linear-gradient(135deg,#c68a66,#7a3c20 50%,#3a1a10)"></div>
  <div class="tile" role="img" aria-label="Black and white portrait of a male violinist" style="left:395px;top:2102px;width:396px;height:282px;background:linear-gradient(120deg,#e8e8e8,#7a7a7a 50%,#1c1c1c)"></div>
  <div class="tile" role="img" aria-label="Concert stage with lights and audience" style="left:395px;top:2384px;width:396px;height:433px;background:radial-gradient(circle at 50% 30%,#f3ead0 0%,#8a6a78 40%,#2a1630 80%)"></div>
  <div class="tile" role="img" aria-label="Rock band performing to a crowd" style="left:791px;top:2102px;width:409px;height:282px;background:linear-gradient(160deg,#8c8a86,#4a4540 50%,#1c1a18)"></div>
  <div class="tile" role="img" aria-label="Guitarist performing with orchestra under stage lights" style="left:791px;top:2384px;width:409px;height:433px;background:radial-gradient(circle at 45% 25%,#e8e6f0 0%,#c0582a 40%,#3a1a12 85%)"></div>
</section>

<footer class="abs footer"></footer>
<div class="foot-head" style="left:171px;top:2878px">Contact Us</div>
<div class="foot-line" style="left:178px;top:2936px;width:270px">
  <svg width="10" height="14" viewBox="0 0 10 14" style="flex:none;margin-top:3px"><path d="M5 0a5 5 0 0 1 5 5c0 3.5-5 9-5 9S0 8.5 0 5a5 5 0 0 1 5-5z" fill="#fff"/><circle cx="5" cy="5" r="2" fill="#222"/></svg>
  <span>121A, Itaque earum rerum hic tenetur sapiente delectus</span></div>
<div class="foot-line" style="left:178px;top:2990px">
  <svg width="12" height="12" viewBox="0 0 12 12" style="flex:none;margin-top:4px"><path d="M2 0l3 3-1.5 1.5a7 7 0 0 0 4 4L9 7l3 3-2 2C5 12 0 7 0 2z" fill="#fff"/></svg>
  <span>000 - 0000 - 0000</span></div>
<div class="foot-line" style="left:178px;top:3022px">
  <svg width="13" height="10" viewBox="0 0 13 10" style="flex:none;margin-top:5px"><rect width="13" height="10" fill="#fff"/><path d="M0 0l6.5 5L13 0" stroke="#222" fill="none"/></svg>
  <span>info@eemvalleiorkest.example</span></div>
<div class="abs foot-social"><span></span><span></span><span></span></div>

<div class="foot-head" style="left:465px;top:2878px">Newsletter</div>
<div class="foot-line" style="left:464px;top:2936px">Join Our Newsletter &amp; Get All Updates!</div>
<div class="abs email-field">Email...</div>
<div class="abs subscribe">SUBSCRIBE</div>

<div class="abs page-box">
  <div class="page-cover" role="img" aria-label="Orchestra violinists cover photo"></div>
  <div class="page-thumb"></div>
  <div class="page-name">Eemvallei Orkest</div>
  <div class="page-likes">38,648 likes</div>
  <div class="mini-btn" style="left:10px">Like Page</div>
  <div class="mini-btn" style="left:236px">Share</div>
  <div class="friends">Be the first of your friends to like this
    <div class="faces"><span></span><span></span><span></span><span></span><span></span><span></span><span></span><span></span><span></span></div>
  </div>
</div>

<div class="abs copyright">©Copyright information here</div>
</body>
</html>
```